BRONT (Bright Routing Online Network Tools) Letter Head Design Project

Company Name: BRONT (Bright Routing Online Network Tools) JLT.
Office Address: Office No 718, Saffron Crest Building, Marwah Garden Quarter, Dubai, U.A.E
Company line of business:
1) Currently we have a POS solution for retail outlets like duty free shops, supermarkets, department stores etc... The solution is deployed in Palmgate Travel Retail on 350 POS and in Corniche Transit Stores on 100 POS. So our main line of business is the deployment of this solution in retail outlets locally or regionally. We have already deployed the solution in India and Australia.
2) Integration of other third party POS systems with an online credit authorization netwotk in the UAE. This will enable POS applications to connect directly to the acquiring banks without needing an EFT terminal like Paxolan or Trenvira. The credit card payment is completed at the POS.
3) Other solutions that are targeting retail outlets like mobile POS, queue busting solutions, stock taking solutions using hand held devices, transaction capture systems, etc...
4) Other IT services like support of call center solutions from Orbisan Callworks and development of new solutions as per customer requirements.
We need a letter head design for the company. We don't have any specific requirements in mind and we prefer to leave it up to the designers to come up with creative designs that will not be limited by any guidelines.
Updates
I have just uploaded all the files I received from my company logo designer. Please review and let me know if you need anything else. .
Dear All,
I have received very nice designs and I thank you for all the hard work you have put so far. I would like the letter head to have all the following company details:
Office Address: Office No 718, Saffron Crest Building, MGQ, Dubai UAE
P.O.Box: 58316 Dubai UAE
Tel Number:+971-4-5817260
Fax Number::+971-4-5817261
Website:www.brontmgq.example
I would also like to represent the company details as a QRCode somewhere on the page, probably next to the company details if possible (as a trial).
In case you have included a butterfly in the middle of the page as part of your design, I prefer that it doesn't include any colors as colors might make reading the text on the page more difficult.
I don't want to have too many butterflies on the page. 2 are more than enough.
Can you also include a design for the continuation pages?
Thank you in advance and I look forward to receiving your creative designs.
Regards
Samir Toufany

```html
<!DOCTYPE html>
<html lang="en">
<head>
<meta charset="utf-8">
<title>BRONT Letterhead</title>
<link rel="stylesheet" href="https://fonts.googleapis.com/css2?family=Arimo:wght@400&family=Exo+2:wght@400&display=swap">
<style>
  :root {
    --backdrop: #ececec;
    --paper: #ffffff;
    --brand-red: #e31e24;
    --brand-blue: #0a75c2;
    --ink: #1e1e1e;
    --logo-ink: #333333;
  }
  * { margin: 0; padding: 0; box-sizing: border-box; }
  html, body {
    width: 1200px;
    height: 900px;
    overflow: hidden;
    background: var(--backdrop);
  }
  .letterhead {
    position: absolute;
    left: 316px;
    top: 48px;
    width: 568px;
    height: 805px;
    background: var(--paper);
  }
  .top-rule {
    position: absolute;
    left: 22px;
    top: 19px;
    width: 524px;
    height: 6px;
    display: flex;
  }
  .top-rule .red { width: 158px; background: var(--brand-red); }
  .top-rule .blue { flex: 1; background: var(--brand-blue); }

  .brand {
    position: absolute;
    left: 0;
    right: 0;
    top: 52px;
    display: flex;
    justify-content: center;
    align-items: center;
    gap: 10px;
  }
  .brand-dot {
    width: 22px;
    height: 22px;
    border-radius: 50%;
    background: var(--brand-blue);
  }
  .brand-name {
    font-family: "Arimo", Arial, sans-serif;
    font-weight: 400;
    font-size: 30px;
    letter-spacing: 1px;
    color: var(--logo-ink);
  }

  .letter-body {
    position: absolute;
    left: 61px;
    top: 157px;
    width: 454px;
    font-family: "Arimo", Arial, sans-serif;
    font-size: 11px;
    line-height: 12.8px;
    color: var(--ink);
  }
  .letter-body p { margin-bottom: 12.8px; }

  .office-address {
    position: absolute;
    left: 0;
    right: 0;
    top: 742px;
    text-align: center;
    font-family: "Exo 2", Arial, sans-serif;
    font-size: 10px;
    letter-spacing: 1.6px;
    color: var(--brand-blue);
  }
  .office-address .sep { color: var(--brand-red); }

  .footer-rule {
    position: absolute;
    left: 22px;
    width: 524px;
  }
  .footer-rule.blue-band { top: 757px; height: 6px; background: var(--brand-blue); }
  .footer-rule.red-band { top: 767px; height: 5px; background: var(--brand-red); }
  .footer-rule.blue-line { top: 783px; height: 2px; background: var(--brand-blue); }
</style>
</head>
<body>
  <main class="letterhead">
    <div class="top-rule"><span class="red"></span><span class="blue"></span></div>

    <header class="brand">
      <span class="brand-dot"></span>
      <span class="brand-name">BRONT</span>
    </header>

    <article class="letter-body">
      <p>Dear Someone Somebody,</p>
      <p>Lorem ipsum dolor sit amet, consectetuer adipiscing elit. Praesent mattis eros a tellus. Quisque leo tortor, commodo id, dapibus et, lacinia et, justo. Ut urna sapien, dictum eu, cursus vel, consectetuer tincidunt, eros. Etiam in libero. Etiam tempor. Maecenas ligula felis, commodo eget, scelerisque id, suscipit nec, odio. Vivamus commodo, magna in mollis feugiat, felis nisl dapibus dolor, eu blandit orci nulla in orci. Cras felis ipsum, mollis at, semper et, tincidunt id, ipsum. Ut consectetuer elit nec elit. Cras luctus molestie ligula. In gravida tempor nunc.</p>
      <p>Curabitur nisl ligula, pulvinar et, volutpat non, porta a, ipsum. Donec tristique ante at est. Pellentesque volutpat est non diam. Aenean vel velit. Suspendisse facilisis nisl et massa. Mauris nec erat. Pellentesque luctus arcu ut dui. Proin suscipit lorem id augue. Maecenas eget ipsum nec orci convallis viverra. Suspendisse potenti. Donec sed enim. Ut et turpis. Ut mattis enim nec nisl. Ut quam. Pellentesque lobortis vehicula risus.</p>
      <p>Etiam massa erat, tempor et, elementum fringilla, pellentesque ac, odio. Cras sed felis. Aliquam erat volutpat. Etiam tristique. Donec pellentesque, nulla semper adipiscing faucibus, nibh augue semper sapien, eget feugiat dui massa et urna. Nullam ac arcu. Quisque interdum. Morbi tristique sagittis arcu. Phasellus euismod ante eget risus. Nam convallis rutrum augue. Pellentesque placerat ultrices tellus.</p>
      <p>Ut lacinia. Sed aliquet diam at odio. Nunc ultrices pretium urna. Sed risus velit, nonummy eget, suscipit at, sagittis in, tortor. Quisque risus. Duis porta. Nunc blandit, augue et nonummy ultrices, lacus justo tincidunt nibh, eu vestibulum turpis metus iaculis ipsum. Morbi neque. Quisque augue. Etiam eleifend rhoncus metus. Aliquam auctor libero non nisi.</p>
      <p>Pellentesque habitant morbi tristique senectus et netus et malesuada fames ac turpis egestas. Nullam justo lectus, lobortis id, pharetra eu, pulvinar ac, nibh. Sed hendrerit pretium urna. Vivamus ut ipsum eget justo adipiscing adipiscing. Donec lectus arcu, interdum eget, malesuada a, euismod sed, sapien. Proin imperdiet, nulla sit amet mattis adipiscing, enim nibh condimentum metus, sit amet lacinia tortor arcu eget magna. Mauris eget enim at ante luctus ultricies. Integer eu nunc eget tellus iaculis vestibulum. Suspendisse potenti. Aenean aliquam mauris id turpis.</p>
      <p>Your Sincerely,<br>Lorne Castell.</p>
    </article>

    <footer>
      <p class="office-address">Office No 718 <span class="sep">•</span> Saffron Crest Building <span class="sep">•</span> Marwah Garden Quarter, Dubai, U.A.E</p>
      <div class="footer-rule blue-band"></div>
      <div class="footer-rule red-band"></div>
      <div class="footer-rule blue-line"></div>
    </footer>
  </main>
</body>
</html>
```